Where the Morning Went: A Season of Turning

The book size is 6x9. I am more interested in an illustrative design like the one I have posted below with a picture of my face and then having elements in the background of a barn, a cross and my little girls eyes peaking out from behind the scenery.
"Where the Morning Went… A Season of Turning" is a gripping memoir of resilience, faith, and courage. Marlene Kostrova’s journey pulls back the curtain on a ranch family fractured by addiction, abuse, and chaos, while revealing an extraordinary path to self-discovery and purpose.
Marlene, her older sister Bettina, and their three younger brothers grow up in a destabilizing environment where frequent moves and changing schools are routine. All the while, they navigate life in the shadow of their father’s addiction, schizophrenia, and violent outbursts. With dark secrets of sexual abuse and domestic violence lurking behind closed doors, the family seems trapped in a cycle of destruction.
Yet, Marlene’s spirit remains unbroken. Anchored by her unshakable belief that God is her true father and Jesus her brother, she clings to her faith and a guiding philosophy she calls “the next right move”—a quiet force that propels her forward, even as those around her fall victim to their demons. As her siblings descend into addiction, incarceration, and heartbreak, Marlene works to protect herself from the same fate while holding onto the family she cherishes.
Described by those who know her as possessing sophisticated grit, Marlene rises above her circumstances with a unique blend of resilience, conscientiousness, and inner grace. She is driven by her belief in “organic truth”—the truth you possess before you are even born—which, once discovered, has the power to set you free into becoming who you were met to be. This profound conviction, along with her commitment to “the next right move,” guides her through life’s darkest moments.
Armed with a PhD in Human Science and experience as a child abuse and neglect investigator, therapist, professor, business leader and coach, Marlene’s true triumph lies in something far deeper: surviving three near-death experiences and realizing that her purpose transcends personal, professional, and material achievements. Rather than pursuing happiness, she dedicates herself to uncovering meaning.
In this inspiring and candid memoir, she invites readers on a journey of becoming—one marked by faith, perseverance, and the courage to listen to the voice of organic truth within. Her story is a testament to the resilience of the human spirit and a beacon of hope for anyone navigating their own path to reclaim their sense of self, purpose, and freedom.

```html
<!DOCTYPE html>
<html lang="en">
<head>
<meta charset="utf-8">
<title>Where the Morning Went – Book Cover</title>
<link rel="stylesheet" href="https://fonts.googleapis.com/css2?family=Cormorant+Garamond:wght@500&family=Montserrat:wght@500&display=swap">
<style>
  :root {
    --page-bg: #ffffff;
    --title-ink: #f4f1f3;
    --subtitle-ink: #f5cbd8;
    --paint-pink: #e83f8c;
    --paint-magenta: #c1449f;
    --paint-violet: #7a4bb0;
    --paint-blue: #2f5d9e;
    --paint-teal: #3f7fa8;
    --paint-peach: #f3a27a;
    --paint-blush: #f2b7c6;
    --portrait-skin: #b98ea8;
    --portrait-hair: #2c3566;
    --portrait-shade: #3a4f8a;
    --dancer-tulle: #e9c3cf;
  }
  html, body {
    margin: 0;
    padding: 0;
    width: 1200px;
    height: 1200px;
    overflow: hidden;
    background: var(--page-bg);
  }
  .canvas {
    position: relative;
    width: 1200px;
    height: 1200px;
  }
  .cover {
    position: absolute;
    left: 240px;
    top: 60px;
    width: 720px;
    height: 1080px;
    overflow: hidden;
    box-shadow: 0 2px 10px rgba(0,0,0,0.08);
  }
  .cover-art {
    position: absolute;
    inset: 0;
    width: 100%;
    height: 100%;
  }
  .author-portrait {
    position: absolute;
    left: 0;
    top: 190px;
    width: 440px;
    height: 890px;
    background:
      radial-gradient(ellipse 120px 170px at 190px 220px, var(--portrait-skin) 0%, rgba(185,142,168,0.75) 55%, rgba(185,142,168,0) 100%),
      radial-gradient(ellipse 170px 260px at 170px 260px, rgba(44,53,102,0.85) 0%, rgba(44,53,102,0.5) 60%, rgba(44,53,102,0) 100%),
      radial-gradient(ellipse 300px 320px at 150px 760px, rgba(58,79,138,0.9) 0%, rgba(58,79,138,0.55) 60%, rgba(58,79,138,0) 100%);
    opacity: 0.85;
  }
  .dancer-illustration {
    position: absolute;
    left: 250px;
    top: 600px;
    width: 300px;
    height: 460px;
    background:
      radial-gradient(ellipse 50px 60px at 150px 70px, rgba(233,195,207,0.8) 0%, rgba(233,195,207,0) 100%),
      radial-gradient(ellipse 140px 120px at 150px 260px, rgba(233,195,207,0.75) 0%, rgba(233,195,207,0.35) 60%, rgba(233,195,207,0) 100%);
  }
  .subtitle {
    position: absolute;
    top: 50px;
    left: 0;
    right: 0;
    text-align: center;
    font-family: "Montserrat", sans-serif;
    font-weight: 500;
    font-size: 24px;
    letter-spacing: 0.3em;
    color: var(--subtitle-ink);
    margin: 0;
  }
  .title {
    position: absolute;
    right: 60px;
    top: 232px;
    margin: 0;
    text-align: right;
    font-family: "Cormorant Garamond", serif;
    font-weight: 500;
    font-size: 114px;
    line-height: 107px;
    color: var(--title-ink);
    letter-spacing: -0.01em;
  }
  .title span { display: block; }
  .author {
    position: absolute;
    left: 0;
    right: 0;
    top: 968px;
    margin: 0;
    text-align: center;
    font-family: "Cormorant Garamond", serif;
    font-weight: 500;
    font-size: 56px;
    letter-spacing: 0.005em;
    color: var(--title-ink);
  }
</style>
</head>
<body>
<div class="canvas">
  <div class="cover">
    <svg class="cover-art" viewBox="0 0 720 1080" preserveAspectRatio="none" role="img" aria-label="Watercolour wash in pink, violet, blue and peach">
      <defs>
        <linearGradient id="wash-base" x1="0" y1="0" x2="0" y2="1">
          <stop offset="0" stop-color="var(--paint-pink)"/>
          <stop offset="0.35" stop-color="var(--paint-magenta)"/>
          <stop offset="0.7" stop-color="var(--paint-violet)"/>
          <stop offset="1" stop-color="var(--paint-teal)"/>
        </linearGradient>
        <radialGradient id="wash-peach" cx="0.85" cy="0.75" r="0.45">
          <stop offset="0" stop-color="var(--paint-peach)" stop-opacity="0.95"/>
          <stop offset="1" stop-color="var(--paint-peach)" stop-opacity="0"/>
        </radialGradient>
        <radialGradient id="wash-blue" cx="0.15" cy="0.85" r="0.5">
          <stop offset="0" stop-color="var(--paint-blue)" stop-opacity="0.9"/>
          <stop offset="1" stop-color="var(--paint-blue)" stop-opacity="0"/>
        </radialGradient>
        <radialGradient id="wash-violet" cx="0.65" cy="0.38" r="0.3">
          <stop offset="0" stop-color="var(--paint-violet)" stop-opacity="0.8"/>
          <stop offset="1" stop-color="var(--paint-violet)" stop-opacity="0"/>
        </radialGradient>
      </defs>
      <rect width="720" height="1080" fill="url(#wash-base)"/>
      <rect width="720" height="1080" fill="url(#wash-violet)"/>
      <rect width="720" height="1080" fill="url(#wash-peach)"/>
      <rect width="720" height="1080" fill="url(#wash-blue)"/>
    </svg>

    <div class="author-portrait" role="img" aria-label="Soft-focus portrait photograph of the author, dark hair, wearing a chain necklace with a padlock, blended into the watercolour"></div>
    <div class="dancer-illustration" role="img" aria-label="Watercolour illustration of a little girl in a pink tutu dancing"></div>

    <p class="subtitle">A SEASON OF TURNING</p>
    <h1 class="title">
      <span>WHERE</span>
      <span>THE</span>
      <span>MORNING</span>
      <span>WENT</span>
    </h1>
    <p class="author">MARLENE KOSTROVA</p>
  </div>
</div>
</body>
</html>
```